Teff Flour Bags

Need simple text, and a small design, in an "Ai File" to eventually be put on a plain brown bag 20lb. I need to send the "AI File" to a company, and they will do the printing onthe bags.

"TEFF FLOUR BROWN" please see uploaded file for samples

```html
<!DOCTYPE html>
<html lang="en">
<head>
<meta charset="utf-8">
<title>Teff Flour Brown – 20 lb Bag Label</title>
<link rel="stylesheet" href="https://fonts.googleapis.com/css2?family=Smokum&family=Source+Serif+4:wght@400;700&family=Archivo+Black&display=swap">
<style>
  :root {
    --kraft: #d8bda1;
    --ink: #111010;
    --ink-soft: #3a2f26;
  }
  html, body {
    margin: 0;
    padding: 0;
    width: 1200px;
    height: 1200px;
    overflow: hidden;
    background: var(--kraft);
  }
  .bag-label {
    display: block;
    width: 1200px;
    height: 1200px;
  }
  .emblem-ring { fill: none; stroke: var(--ink); stroke-width: 8; }
  .emblem-inner-line { fill: none; stroke: var(--ink); stroke-width: 2.5; }
  .established {
    font-family: "Source Serif 4", Georgia, serif;
    font-weight: 400;
    font-size: 27px;
    letter-spacing: 1.5px;
    fill: var(--ink);
  }
  .product-name {
    font-family: "Smokum", "Rye", serif;
    font-size: 200px;
    fill: var(--ink);
  }
  .variant-banner { fill: var(--ink); }
  .variant-name {
    font-family: "Archivo Black", "Arial Black", sans-serif;
    font-size: 80px;
    fill: var(--kraft);
  }
  .net-weight {
    font-family: "Source Serif 4", Georgia, serif;
    font-weight: 700;
    font-size: 30px;
    letter-spacing: 0.5px;
    fill: var(--ink);
  }
</style>
</head>
<body>
<svg class="bag-label" viewBox="0 0 1200 1200" xmlns="http://www.w3.org/2000/svg">
  <defs>
    <linearGradient id="emblem-scene-tone" x1="0" y1="0" x2="0" y2="1">
      <stop offset="0" stop-color="#d8bda1"/>
      <stop offset="0.55" stop-color="#6b5644"/>
      <stop offset="1" stop-color="#111010"/>
    </linearGradient>
  </defs>

  <g class="emblem">
    <ellipse class="emblem-ring" cx="600" cy="378" rx="180" ry="240"/>
    <ellipse class="emblem-scene" cx="600" cy="378" rx="160" ry="218"
             fill="url(#emblem-scene-tone)" role="img"
             aria-label="Illustration of a windmill on a hill with a winding path, sun rays behind it, in black on kraft"/>
    <ellipse class="emblem-inner-line" cx="600" cy="378" rx="160" ry="218"/>
  </g>

  <text class="established" x="600" y="674" text-anchor="middle">ESTABLISHED 2019</text>

  <text class="product-name" x="600" y="842" text-anchor="middle"
        textLength="536" lengthAdjust="spacingAndGlyphs">TEFF FLOUR</text>

  <g class="variant">
    <path class="variant-banner"
          d="M404,876 Q600,846 796,876 L782,930 L796,984 Q600,950 404,984 L424,930 Z"/>
    <text class="variant-name" x="600" y="948" text-anchor="middle"
          textLength="246" lengthAdjust="spacingAndGlyphs">BROWN</text>
  </g>

  <text class="net-weight" x="614" y="1057" text-anchor="middle">Net Weight 20 LBS. ( 9.07kg)</text>
</svg>
</body>
</html>
```